Kanomiva business cards/stationary
Relocation Support Services
I need single sided standard sized Business Card [3.5" x 2"]
Designer's discretion
Professional
Ned Palmer
President
5-31-08 Nishimorino
Suginami-ku, Tokyo 168-0072
ned@kanomiva.com
www.kanomiva.com
Have not yet received logo files from designer. I will be using
Will upload Al format as soon as I receive from designer.
Kanomiva logo to be used

```html
<!DOCTYPE html>
<html lang="en">
<head>
<meta charset="utf-8">
<title>Kanomiva Stationery</title>
<link href="https://fonts.googleapis.com/css2?family=Open+Sans:wght@400;600;700&display=swap" rel="stylesheet">
<style>
:root{
  --red:#d8232a;
  --red-dark:#a3151b;
  --grey:#6d6e71;
  --grey-dark:#3d3e40;
  --ink:#333333;
  --paper:#ffffff;
  --stage:#ecebe8;
  --faint:#f6e6e0;
  --line:#bdbdbd;
}
*{box-sizing:border-box;margin:0;padding:0}
html,body{width:1200px;height:643px;overflow:hidden}
body{background:var(--stage);font-family:"Open Sans",Arial,sans-serif;color:var(--ink);position:relative}
.piece{position:absolute;background:var(--paper);box-shadow:0 2px 6px rgba(0,0,0,.25);overflow:hidden}
.label{position:absolute;font-size:8px;color:#555;white-space:nowrap}
.brand{display:flex;align-items:center;gap:4px;font-weight:700;color:var(--red);line-height:1;white-space:nowrap}
.brand .dot{width:9px;height:9px;border-radius:50%;background:var(--red);flex:none}
.brand.on-dark{color:#fff}
.brand.on-dark .dot{background:#fff}
.swoosh{position:absolute;inset:0;width:100%;height:100%}
/* cards */
.card{width:101px;height:56px;top:29px}
.card .brand{position:absolute;font-size:9px}
.card-front .brand{left:7px;top:7px;font-size:8px;gap:3px}
.card-front .brand .dot{width:7px;height:7px}
.card-front .person{position:absolute;right:24px;top:19px;text-align:right;font-size:4px;line-height:1.3;color:#555}
.card-front .person b{display:block;color:var(--red);font-size:4.6px}
.card-front .contact{position:absolute;left:7px;top:33px;font-size:3.4px;line-height:1.4;color:#555}
.card-center{display:flex;align-items:center;justify-content:center}
.card-center .brand{position:static;font-size:10px}
.card-grey{background:linear-gradient(90deg,var(--grey-dark),#9a9b9e 55%,var(--grey-dark))}
.card-red{background:linear-gradient(90deg,var(--red-dark),var(--red) 50%,var(--red-dark))}
/* sheets */
.sheet{width:331px;height:499px;top:120px}
.sheet .brand{position:absolute;left:26px;top:18px;font-size:14px}
.sheet .brand .dot{width:12px;height:12px}
.watermark{position:absolute;left:60px;top:250px;width:150px;height:150px;border-radius:50%;background:var(--faint);opacity:.7}
.footer{position:absolute;left:20px;right:72px;bottom:12px;font-size:4.6px;color:#666;display:flex;justify-content:space-between;border-top:.5px solid var(--line);padding-top:3px;white-space:nowrap}
.fax-title{position:absolute;right:52px;top:75px;font-size:9px;font-weight:700}
.fax-table{position:absolute;left:22px;top:85px;width:266px;border-collapse:collapse;font-size:5px}
.fax-table td{border:.6px solid #888;height:11px;padding:0 3px}
.fax-table td.key{width:30px}
.fax-checks{position:absolute;left:22px;top:148px;display:flex;gap:16px;font-size:5px}
.fax-checks span::before{content:"";display:inline-block;width:5px;height:5px;border:.6px solid #555;margin-right:3px;vertical-align:-1px}
/* envelopes */
.envelope{left:749px}
.env-front{top:38px;width:427px;height:173px}
.env-front .brand{position:absolute;left:18px;top:16px;font-size:14px}
.env-front .brand .dot{width:12px;height:12px}
.env-front .return{position:absolute;left:18px;top:36px;font-size:4.6px;color:#666;line-height:1.4}
.env-back{width:427px;height:168px;background:transparent;box-shadow:none;overflow:visible}
.env-back svg{position:absolute;inset:0;width:100%;height:100%;overflow:visible;filter:drop-shadow(0 2px 3px rgba(0,0,0,.25))}
.env-back .brand{position:absolute;left:50%;transform:translateX(-50%);font-size:13px}
</style>
</head>
<body>

<!-- business cards -->
<div class="label" style="left:48px;top:18px">Business Cards</div>
<div class="piece card card-front" style="left:48px">
  <svg class="swoosh" viewBox="0 0 101 56" preserveAspectRatio="none" aria-hidden="true">
    <path d="M82 0H101V56H93C100 38 98 16 82 0Z" fill="var(--red)"/>
  </svg>
  <div class="brand"><span class="dot"></span>Kanomiva</div>
  <div class="person"><b>Ned Palmer</b>President</div>
  <div class="contact">5-31-08 Nishimorino<br>Suginami-ku, Tokyo 168-0072<br>ned@kanomiva.com<br>www.kanomiva.com</div>
</div>
<div class="piece card card-center" style="left:163px">
  <div class="brand"><span class="dot"></span>Kanomiva</div>
</div>
<div class="piece card card-center card-grey" style="left:343px">
  <div class="brand on-dark"><span class="dot"></span>Kanomiva</div>
</div>
<div class="piece card card-center card-red" style="left:470px">
  <div class="brand on-dark"><span class="dot"></span>Kanomiva</div>
</div>

<!-- fax cover -->
<div class="label" style="left:186px;top:108px">Fax Cover</div>
<div class="piece sheet" style="left:48px">
  <svg class="swoosh" viewBox="0 0 331 499" preserveAspectRatio="none" aria-hidden="true">
    <defs><linearGradient id="greyFade" x1="0" y1="0" x2="0" y2="1"><stop offset="0" stop-color="#ffffff"/><stop offset="1" stop-color="var(--grey)"/></linearGradient></defs>
    <path d="M262 0H331V330C324 190 305 80 262 0Z" fill="var(--red)"/>
    <path d="M331 150C326 290 308 400 268 499H331Z" fill="url(#greyFade)"/>
  </svg>
  <div class="brand"><span class="dot"></span>Kanomiva</div>
  <div class="fax-title">FAX</div>
  <table class="fax-table">
    <tr><td class="key">To:</td><td></td><td class="key">From:</td><td></td></tr>
    <tr><td class="key">Fax:</td><td></td><td class="key">Pages:</td><td></td></tr>
    <tr><td class="key">Phone:</td><td></td><td class="key">Date:</td><td></td></tr>
    <tr><td class="key">Re:</td><td></td><td class="key">CC:</td><td></td></tr>
  </table>
  <div class="fax-checks"><span>Urgent</span><span>For Review</span><span>Please Comment</span><span>Please Reply</span><span>Please Recycle</span></div>
  <div class="watermark" role="img" aria-label="Faint brand mark decoration"></div>
  <div class="footer"><span>5-31-08 Nishimorino, Suginami-ku, Tokyo 168-0072</span><span>T: +81 3 5550 4182</span><span>www.kanomiva.com</span></div>
</div>

<!-- letterhead -->
<div class="label" style="left:540px;top:108px">Letterhead</div>
<div class="piece sheet" style="left:398px">
  <svg class="swoosh" viewBox="0 0 331 499" preserveAspectRatio="none" aria-hidden="true">
    <path d="M262 0H331V330C324 190 305 80 262 0Z" fill="var(--red)"/>
    <path d="M331 150C326 290 308 400 268 499H331Z" fill="url(#greyFade)"/>
  </svg>
  <div class="brand"><span class="dot"></span>Kanomiva</div>
  <div class="watermark" role="img" aria-label="Faint brand mark decoration"></div>
  <div class="footer"><span>5-31-08 Nishimorino, Suginami-ku, Tokyo 168-0072</span><span>T: +81 3 5550 4182</span><span>ned@kanomiva.com</span></div>
</div>

<!-- envelope front -->
<div class="label" style="left:1050px;top:27px">Envelopes (Front)</div>
<div class="piece envelope env-front">
  <svg class="swoosh" viewBox="0 0 427 173" preserveAspectRatio="none" aria-hidden="true">
    <path d="M340 0H427V120C415 70 385 25 340 0Z" fill="var(--red)"/>
    <path d="M427 60C420 110 400 150 370 173H427Z" fill="url(#greyFade)"/>
  </svg>
  <div class="brand"><span class="dot"></span>Kanomiva</div>
  <div class="return">5-31-08 Nishimorino<br>Suginami-ku, Tokyo 168-0072</div>
</div>

<!-- envelopes back -->
<div class="label" style="left:1020px;top:272px">Envelopes Option 1 (Back)</div>
<div class="piece envelope env-back" style="top:284px">
  <svg viewBox="0 0 427 168" preserveAspectRatio="none" aria-hidden="true">
    <rect width="427" height="168" fill="#fff"/>
    <path d="M0 0H427L250 70Q213 84 177 70Z" fill="#fafafa" stroke="#ddd" stroke-width=".8"/>
  </svg>
  <div class="brand" style="top:30px"><span class="dot"></span>Kanomiva</div>
</div>

<div class="label" style="left:1020px;top:362px">Envelopes Option 2 (Back)</div>
<div class="piece envelope env-back" style="top:375px;left:772px;width:404px;height:150px">
  <svg viewBox="0 0 404 150" preserveAspectRatio="none" aria-hidden="true">
    <rect width="404" height="150" fill="#fff"/>
    <path d="M0 0H404L236 62Q202 74 168 62Z" fill="var(--grey)"/>
  </svg>
  <div class="brand on-dark" style="top:22px"><span class="dot"></span>Kanomiva</div>
</div>

<div class="label" style="left:1020px;top:423px">Envelopes Option 3 (Back)</div>
<div class="piece envelope env-back" style="top:436px;left:810px;width:366px;height:165px">
  <svg viewBox="0 0 366 165" preserveAspectRatio="none" aria-hidden="true">
    <rect width="366" height="165" fill="#fff"/>
    <path d="M0 0H366L214 66Q183 78 152 66Z" fill="var(--red)"/>
  </svg>
  <div class="brand on-dark" style="top:24px"><span class="dot"></span>Kanomiva</div>
</div>

</body>
</html>
```